RW Frameworks Inc Business cards

We need business cards using our existing logo but slightly modified. Right now the logo says RW Framework Masonry. We want to keep the RW part of the design, but replace the Framework Masonry portion with "FRAMEWORKS". Please see the attached file.
Ideally this would be a blank template so we can add Different Names, titles, and phone numbers later.
On the one side we want only the logo and on the other side the detail. I'm attaching an example for you to see.
Please reach out with any other questions. Our address and other details will be given out once we find a design we like.

Target Market(s)

Construction Industry

```html
<!DOCTYPE html>
<html lang="en">
<head>
<meta charset="utf-8">
<title>RW Frameworks Inc — Business Cards</title>
<link rel="stylesheet" href="https://fonts.googleapis.com/css2?family=Open+Sans:wght@400;600;700&display=swap">
<style>
  :root {
    --brand-blue: #1c76bb;
    --ink: #111111;
    --rule-grey: #838386;
    --card-edge: #8a8a8a;
    --paper: #ffffff;
  }
  * { margin: 0; padding: 0; box-sizing: border-box; }
  html, body {
    width: 1200px; height: 1200px; overflow: hidden;
    background: var(--paper);
    font-family: "Open Sans", sans-serif;
  }
  .sheet { position: relative; width: 1200px; height: 1200px; }

  .card { position: absolute; left: 217px; width: 773px; height: 472px; }
  .card--front { top: 93px; background: var(--paper); border: 1px solid var(--card-edge); border-bottom: none; }
  .card--back { top: 642px; background: var(--brand-blue); }

  .wordmark {
    position: absolute; font-weight: 700; white-space: nowrap;
    transform: translate(-50%, -50%); letter-spacing: 0.5px;
  }
  .card--front .wordmark { left: 206px; top: 219px; font-size: 30px; color: var(--brand-blue); }
  .card--back .wordmark { left: 50%; top: 224px; font-size: 52px; color: var(--paper); }

  .divider {
    position: absolute; left: 385px; top: 124px;
    width: 4px; height: 169px; background: var(--rule-grey);
  }

  .person { position: absolute; left: 414px; top: 108px; }
  .person__name { font-size: 29px; font-weight: 700; color: var(--brand-blue); line-height: 1.05; letter-spacing: 0.3px; }
  .person__title { font-size: 25px; font-weight: 400; color: var(--ink); line-height: 1.15; }

  .contacts { position: absolute; left: 413px; top: 197px; list-style: none; }
  .contacts__item { display: flex; align-items: center; height: 34px; font-size: 25px; color: var(--ink); }
  .contacts__icon { width: 26px; height: 26px; margin-right: 12px; flex: none; }

  .address-band {
    position: absolute; left: -1px; right: -1px; bottom: 0; height: 74px;
    background: var(--brand-blue); color: var(--paper);
    display: flex; align-items: center; justify-content: center;
    font-size: 24px; font-weight: 400;
  }
</style>
</head>
<body>
<main class="sheet">

  <section class="card card--front" aria-label="Business card, details side">
    <div class="wordmark">RW Frameworks</div>
    <div class="divider"></div>

    <div class="person">
      <p class="person__name">PERSON NAME</p>
      <p class="person__title">Manager</p>
    </div>

    <ul class="contacts">
      <li class="contacts__item">
        <svg class="contacts__icon" viewBox="0 0 26 26" aria-hidden="true">
          <circle cx="13" cy="13" r="13" fill="var(--brand-blue)"/>
          <path d="M8.6 7.2l2.3-.4 1.2 2.9-1.5 1.2c.8 1.7 2 2.9 3.6 3.7l1.3-1.5 2.9 1.2-.4 2.3c-.2.6-.8 1-1.5.9C11.4 17 8.8 14.4 7.5 9.2c-.1-.8.4-1.7 1.1-2z" fill="var(--paper)"/>
        </svg>
        +91 9000012345
      </li>
      <li class="contacts__item">
        <svg class="contacts__icon" viewBox="0 0 26 26" aria-hidden="true">
          <circle cx="13" cy="13" r="13" fill="var(--brand-blue)"/>
          <rect x="6" y="8.5" width="14" height="9" fill="none" stroke="var(--paper)" stroke-width="1.4"/>
          <path d="M6 8.5l7 5.5 7-5.5M6 17.5l5-4.5M20 17.5l-5-4.5" fill="none" stroke="var(--paper)" stroke-width="1.2"/>
        </svg>
        info@rwframeworks.com
      </li>
      <li class="contacts__item">
        <svg class="contacts__icon" viewBox="0 0 26 26" aria-hidden="true">
          <circle cx="13" cy="13" r="13" fill="var(--brand-blue)"/>
          <g fill="none" stroke="var(--paper)" stroke-width="1.2">
            <circle cx="13" cy="13" r="7"/>
            <ellipse cx="13" cy="13" rx="3" ry="7"/>
            <path d="M6 13h14M7 9.5h12M7 16.5h12"/>
          </g>
        </svg>
        www.rwframeworks.com
      </li>
    </ul>

    <footer class="address-band">18, Rose Villa, Mill Road, Eastfield</footer>
  </section>

  <section class="card card--back" aria-label="Business card, logo side">
    <div class="wordmark">RW Frameworks</div>
  </section>

</main>
</body>
</html>
```